Uncoded front page web design for wedding and event planning company

Hi.

I am launching a wedding and event planning company called Silver Fern Gatherings and need a professional and appealing web design.

So, let me explain my company. I am based in Swindon in Wiltshire but the company will plan weddings and events in Oxfordshire, Wiltshire, Berkshire and London.

We will plan weddings, birthdays, conferences, product launches, fashion shows and conventions but the main focus of the website at this stage should be the weddings with all the other occasions being covered under a single 'events' heading.

My contact details for the website should be:
Marion Blake
marion@silverferngatherings.co.uk
01632 960457 / 07700 900583

I'd like the website to feel clean, bright and elegant and be set against a white or off-white background. My logo is purple and I'd therefore like some purple incorporated into the design although feel free to use a more muted purple as my one might be a little bright? I'm also considering whether it would look nice paired with a little of the colour gold - maybe as a font colour in places?? I'll leave you to figure that one out as your design eye will be better than mine but for your reference below is my purple colour and my suggested gold one....

My purple colour is Pantone 2592 C but feel free to use others
My suggested gold I'm looking at is Pantone 14-1041 TCX

I would like to incorporate a Friendlink feed in the front page if possible, if it looks right. I'd also like to include a variety of pictures as well so I've included a few in a Dropbox folder which is linked below. Please don't feel obliged to use them all by any means (there's loads!) but you've got a few there to play with. If you find any other royalty free images you'd rather use please go ahead but on the understanding I can have them afterwards!

My logo can be retrieved via this Dropbox link...
You'll notice there are 2 styles of placement. Please feel free to use either to fit in with your design...
https://www.filedrawer-example.com/sh/qk7pa2mwx9rn4lt/BBBKzq8ohPnvve4S03LoPjvb?dl=0

The wedding images I have are in this Dropbox folder...
https://www.filedrawer-example.com/sh/m8wd6rzp2lo4ye1/BBB4kqrXv8nWd7S05JmOgtlp?dl=0

Other than that, it's over to you.... I can't wait to receive your designs :-)

Ooh....finally just to say, as I receive designs in I think I'll notice aspects that I like and don't like and if I feel they'll be useful for other designers, I'll update my brief below. Thanks

BRIEF UPDATE:
Someone asked if I had a tag-line. Could you use "Creating exquisite occasions today for amazing memories tomorrow"

I realise I hadn't explained what I'd like included on my home page so here's some notes to consider....

A welcome to section for me to start narrative about us and our services which has a button that links to our 'about us' page and 'services' page for further information.

A section that nicely illustrates what services we offer whether that be with icons or pictures.

A section with some photos in that would link to our gallery

A section that shows some customer reviews and blog entries that would link to my reviews page and blog to read more.

And finally a contact us section with my details, social media links and site map.

***
I also need to draw attention to where in the UK my services cover. I was therefore thinking perhaps we could use a picture to demonstrate this where it highlights Wiltshire, Oxfordshire, Berkshire and London on a map thereby demonstrating our areas covered. I have found several English county maps when searching on Google but I'm not sure how to highlight the areas I cover (or dull out the areas I don't) so if you have any ideas on this, I'd really like it incorporated. Thanks. (by the way, for those of you not familiar with English counties, the ones I cover are often abbreviated to Wilts, Oxon, Berks, London, so if you find a suitable map with those names on rather than the full names, you'll know what they are!)

I've found an image of the county map which might work well. I was wondering whether we might somehow grey out the counties I don't cover and just keep the ones I do as mentioned above and then crop it into perhaps a shadowed circle? I've attached a screenshot to the brief.
Updates

I've decided on the tag-line "Creating exquisite occasions today for amazing memories tomorrow" so if that could be included somewhere that would be great. I also need to draw attention to where in the UK my services cover. I was therefore thinking perhaps we could use a picture to demonstrate this where it highlights Wiltshire, Oxfordshire, Berkshire and London on a map thereby demonstrating our areas covered. I have found several English county maps when searching on Google but I'm not sure how to highlight the areas I cover (or dull out the areas I don't) so if you have any ideas on this, I'd really like it incorporated. Thanks. Added Wednesday, June 24, 2015

Target Market(s)

Predominately women aged 25-55

Industry/Entity Type

Wedding Planner

Number of Pages Required

1 page

Font styles to use
Sans Serif
Script

Requirements
Nice to have
• I'd like to see how the colour theme of purple and perhaps a little gold (maybe as a font colour) look against a white background. I've mentioned the Pantone colours in the brief above.
• I've attached a screenshot of a webpage with gold writing in and fonts that I like. Perhaps it could give you inspiration?
Should not have
• I really don't like the font QUILLORA so please done use that.

```html
<!DOCTYPE html>
<html lang="en">
<head>
<meta charset="utf-8">
<title>Silver Fern Gatherings – Weddings &amp; Events</title>
<link rel="stylesheet" href="https://fonts.googleapis.com/css2?family=Cinzel:wght@400;700&family=Questrial&display=swap">
<style>
:root{
  --purple:#9a2c9c;
  --purple-soft:#b56ab8;
  --gold:#e2a53c;
  --gold-line:#e9c48a;
  --ink:#222222;
  --grey:#6d6d6d;
  --sand:#f3e6d6;
  --white:#ffffff;
}
*{box-sizing:border-box;margin:0;padding:0}
html,body{width:980px;height:1200px;overflow:hidden}
body{position:relative;font-family:'Questrial',sans-serif;color:var(--ink);background:#f6f1ee}
.backdrop{position:absolute;inset:0;
  background:
    radial-gradient(ellipse 170px 130px at 50px 555px,#d9a95a 0%,#e8c58e 40%,rgba(240,225,205,0) 100%),
    radial-gradient(ellipse 260px 320px at 70px 1030px,#f0b9c5 0%,rgba(244,206,214,.6) 45%,rgba(246,241,238,0) 100%),
    radial-gradient(ellipse 260px 300px at 930px 1000px,#f4c2c4 0%,rgba(246,214,214,.5) 50%,rgba(246,241,238,0) 100%),
    radial-gradient(ellipse 250px 260px at 890px 240px,#eef0de 0%,rgba(245,240,230,0) 100%),
    linear-gradient(180deg,#f7f4f2 0%,#f3ece9 60%,#f4dcdf 100%)}
.column{position:absolute;left:132px;top:0;width:717px;height:1200px;background:rgba(255,255,255,.55)}
.header-shape,.footer-shape{position:absolute;left:0;width:717px}
.header-shape{top:0;height:130px}
.ghost-title{position:absolute;top:32px;font-family:'Cinzel',serif;font-size:33px;color:#f3e2d3;letter-spacing:1px}
.ghost-left{left:44px}.ghost-right{left:524px}
.brand{position:absolute;top:62px;left:233px;width:250px;text-align:center;font-family:'Cinzel',serif;font-size:17px;line-height:21px;color:var(--purple)}
.brand-dot{display:block;margin:0 auto 6px;width:30px;height:30px;border-radius:50%;background:var(--purple-soft);opacity:.55}
.nav{position:absolute;top:127px;left:18px;width:681px;height:14px;border-top:1px solid #777;border-bottom:1px solid #777;display:flex;justify-content:space-between;align-items:center;font-family:'Cinzel',serif;font-size:11.4px;color:var(--purple)}
.nav .link{text-decoration:underline;text-underline-offset:1px}
.nav .sep{color:#555}
.intro{position:absolute;top:151px;left:17px;width:682px;height:124px;border:1px solid var(--gold-line);border-radius:22px;background:rgba(255,255,255,.8);text-align:center;color:var(--gold);font-size:11.4px;line-height:13.3px;padding:14px 70px 0}
.intro .lead{font-size:12px}
.intro p+p{margin-top:13px}
.intro u{color:#d18e26}
.card{position:absolute;top:310px;width:333px;height:315px;border:1px solid var(--gold-line);border-radius:10px;background:#fff;overflow:hidden}
.card-weddings{left:17px}.card-events{left:366px}
.card-photo{position:absolute;left:0;top:0;width:100%;height:200px}
.card-weddings .card-photo{background:linear-gradient(180deg,#cfc7c3 0%,#e7e0dc 45%,#ffffff 100%)}
.card-events .card-photo{background:linear-gradient(180deg,#c4b8b2 0%,#e6dcda 45%,#ffffff 100%)}
.card h2{position:relative;text-align:center;font-family:'Cinzel',serif;font-weight:400;font-size:31px;margin-top:20px;letter-spacing:.5px;color:#2a2a2a}
.quote{position:relative;margin:6px 38px 0;text-align:center;font-style:italic;font-size:12.4px;line-height:15px;color:#222}
.quote::before,.quote::after{position:absolute;font-family:'Cinzel',serif;font-size:22px;font-style:normal;color:#555;top:-8px}
.quote::before{content:"\201C";left:-2px}.quote::after{content:"\201D";right:-2px}
.quote cite{display:block;font-size:9.8px;margin-top:1px}
.card-body{position:absolute;left:17px;right:14px;top:162px;font-size:11.4px;line-height:13.3px;color:#1e1e1e}
.card-body p+p{margin-top:13px}
.card-body u{text-underline-offset:1px}
.gallery{position:absolute;top:684px;left:17px;width:682px;height:314px;border:1px solid var(--gold-line);border-radius:12px;background:#fff}
.gallery h2{text-align:center;font-family:'Cinzel',serif;font-weight:400;font-size:31px;color:var(--gold);margin-top:19px;letter-spacing:1px}
.thumb{position:absolute;width:100px;height:100px;border:1px solid var(--gold-line);padding:6px;background:#fff}
.thumb span{display:block;width:100%;height:100%}
.arrow{position:absolute;top:163px;width:14px;height:20px}
.footer-shape{top:1020px;height:150px}
.quote-button{position:absolute;top:1021px;left:271px;width:174px;height:88px;border-radius:50%;border:2px solid var(--purple-soft);background:#fff;box-shadow:inset 0 0 0 4px #fff,inset 0 0 0 5px #e6c9e7;display:flex;align-items:center;justify-content:center;text-align:center;font-family:'Cinzel',serif;font-size:15.5px;line-height:18px;color:var(--purple)}
.social{position:absolute;text-align:right;font-size:11.8px;color:var(--gold);display:flex;align-items:center;gap:10px;white-space:nowrap}
.social i{display:inline-block;width:14px;height:14px;border-radius:50%;border:1.5px solid var(--gold)}
.contact{position:absolute;left:478px;font-size:11.8px;color:var(--gold);display:flex;align-items:center;gap:8px;white-space:nowrap}
.contact svg{width:18px;height:18px}
.base-nav{position:absolute;top:1170px;left:0;width:717px;height:30px;background:var(--sand);display:flex;justify-content:space-between;align-items:center;padding:0 28px 0 21px;font-family:'Cinzel',serif;font-size:11.6px;color:var(--grey)}
</style>
</head>
<body>
<div class="backdrop" role="img" aria-label="Soft focus wedding photograph: gold rings and pink flowers on a pale background"></div>

<main class="column">
  <svg class="header-shape" viewBox="0 0 717 130" aria-hidden="true">
    <path d="M0 0H717V85Q600 92 470 100C452 100 470 12 358 12C246 12 264 100 247 100Q120 92 0 85Z" fill="#fff"/>
    <path d="M0 85Q120 92 247 100C264 100 246 12 358 12C470 12 452 100 470 100Q600 92 717 85" fill="none" stroke="#ecd3b4" stroke-width="1"/>
  </svg>
  <div class="ghost-title ghost-left">WEDDINGS</div>
  <div class="ghost-title ghost-right">EVENTS</div>
  <div class="brand"><span class="brand-dot"></span>Silver Fern Gatherings</div>

  <nav class="nav">
    <span class="link">Weddings</span><span class="sep">/</span>
    <span class="link">Birthdays</span><span class="sep">/</span>
    <span class="link">Conferences</span><span class="sep">/</span>
    <span class="link">Product Launches</span><span class="sep">/</span>
    <span class="link">Fashion Shows</span><span class="sep">/</span>
    <span class="link">Conventions</span>
  </nav>

  <section class="intro">
    <p><span class="lead">Silver Fern Gatherings plan weddings and events in Oxfordshire, Wiltshire, Berkshire and London.</span><br>
    Lorem ipsum dolor sit amet, consectetuer adipiscing elit. Suspendisse hendrerit ligula quis velit pharetra egestas. Ut molestie elit non massa. Vivamus tincidunt bibendum velit. Quisque nisl diam, nonummy eu, lobortis consequat, mollis ut, tellus. In iaculis. <u>This is a link.</u></p>
    <p>Etiam sagittis nulla at quam. In massa. Integer leo tortor, dignissim nec, volutpat id, luctus non, nisi. Morbi iaculis mollis felis. Ut ullamcorper tortor. <u>Read More.</u></p>
  </section>

  <article class="card card-weddings">
    <div class="card-photo" role="img" aria-label="Faded photograph of a bride holding hands with the groom"></div>
    <h2>WEDDINGS</h2>
    <blockquote class="quote">Wonderful wedding planner, made it effortless,extremely attractive and a rosounding success!<cite>— Anna Perrin</cite></blockquote>
    <div class="card-body">
      <p>Etiam varius sapien in turpis. Suspendisse eros nibh, cursus vel, malesuada id, ullamcorper et, odio. Proin ac velit et ligula aliquam molestie. Proin congue sapien eget nunc. Sed at orci. Aenean ornare, velit eget bibendum adipiscing, turpis ante cursus mauris, in porta dolor mauris eget mi.</p>
      <p>Nulla tincidunt semper lorem. Nunc vitae urna eget mi convallis iaculis. Ut tincidunt ullamcorper lectus. Integer interdum, nisi ac sollicitudin rhoncus, quam nisl mollis enim, eget condimentum erat purus eu orci.</p>
    </div>
  </article>

  <article class="card card-events">
    <div class="card-photo" role="img" aria-label="Faded photograph of guests dining at a dressed event table"></div>
    <h2>EVENTS</h2>
    <blockquote class="quote">Excellent event planner, very creative, pays attention to all the details and would not hesitate to use again!<cite>— Daniel R. Moss</cite></blockquote>
    <div class="card-body">
      <p>Etiam varius sapien in turpis. Suspendisse eros nibh, cursus vel, malesuada id, ullamcorper et, odio. Proin ac velit et ligula aliquam molestie. Proin congue sapien eget nunc. Sed at orci. Aenean ornare, velit eget bibendum adipiscing, turpis ante cursus mauris, in porta dolor mauris eget mi. <u>This is another link.</u></p>
      <p>Nulla tincidunt semper lorem. Nunc vitae urna eget mi convallis iaculis. Ut tincidunt ullamcorper lectus. Integer interdum, nisi ac sollicitudin rhoncus, quam nisl mollis enim, eget condimentum erat purus eu orci.</p>
    </div>
  </article>

  <section class="gallery">
    <h2>GALLERY</h2>
    <svg class="arrow" style="left:28px" viewBox="0 0 14 20" aria-hidden="true"><path d="M12 2L3 10L12 18" fill="none" stroke="#e2a53c" stroke-width="3"/></svg>
    <svg class="arrow" style="left:642px" viewBox="0 0 14 20" aria-hidden="true"><path d="M2 2L11 10L2 18" fill="none" stroke="#e2a53c" stroke-width="3"/></svg>

    <div class="thumb" style="left:59px;top:67px"><span role="img" aria-label="Pink and white bridal bouquet" style="background:linear-gradient(135deg,#f1d7de,#d8849f 55%,#9fb07a)"></span></div>
    <div class="thumb" style="left:175px;top:67px"><span role="img" aria-label="Bride in a lace dress holding flowers" style="background:linear-gradient(135deg,#e4e0dc,#c9bdb4 60%,#f3f0ec)"></span></div>
    <div class="thumb" style="left:292px;top:67px"><span role="img" aria-label="Couple embracing beside white flowers" style="background:linear-gradient(135deg,#c6c6c4,#a7a59e 50%,#eceae4)"></span></div>
    <div class="thumb" style="left:408px;top:67px"><span role="img" aria-label="Couple signing the wedding register" style="background:linear-gradient(135deg,#34415e,#7d8bab 50%,#f2efe9)"></span></div>
    <div class="thumb" style="left:525px;top:67px"><span role="img" aria-label="Cream and pink rose posy" style="background:linear-gradient(135deg,#f7f4f0,#efcfcf 55%,#dfe6cf)"></span></div>

    <div class="thumb" style="left:59px;top:184px"><span role="img" aria-label="Bouquet resting on a wooden table" style="background:linear-gradient(135deg,#efe6e0,#d9a2ae 50%,#7a5a45)"></span></div>
    <div class="thumb" style="left:175px;top:184px"><span role="img" aria-label="Champagne bottle in an ice bucket" style="background:linear-gradient(135deg,#efe7dc,#c9a666 55%,#f5efe4)"></span></div>
    <div class="thumb" style="left:292px;top:184px"><span role="img" aria-label="Reception room laid with white tables" style="background:linear-gradient(180deg,#a08f6a,#d8d2c4 50%,#f3f1ee)"></span></div>
    <div class="thumb" style="left:408px;top:184px"><span role="img" aria-label="Back of a corseted wedding dress being laced" style="background:linear-gradient(135deg,#d8d3cc,#f5f3f0 55%,#cfc8bf)"></span></div>
    <div class="thumb" style="left:525px;top:184px"><span role="img" aria-label="Bride having her hair styled" style="background:linear-gradient(135deg,#4b2f2a,#b68a78 50%,#e8d8d6)"></span></div>
  </section>

  <svg class="footer-shape" viewBox="0 0 717 150" aria-hidden="true">
    <path d="M0 25Q120 15 247 10C264 10 246 112 358 112C470 112 452 10 470 10Q600 15 717 25V150H0Z" fill="#fff"/>
    <path d="M0 25Q120 15 247 10C264 10 246 112 358 112C470 112 452 10 470 10Q600 15 717 25" fill="none" stroke="#ecd3b4" stroke-width="1"/>
  </svg>
  <div class="quote-button">CLICK FOR AN<br>ONLINE QUOTE</div>

  <div class="social" style="top:1083px;right:482px">Follow us on Friendlink <i></i></div>
  <div class="social" style="top:1109px;right:455px">Read our tweets and post on Chirper <i></i></div>
  <div class="social" style="top:1132px;right:416px">Connect with us on Worknet <i></i></div>

  <div class="contact" style="top:1082px">
    <svg viewBox="0 0 18 18" aria-hidden="true"><circle cx="9" cy="6" r="4" fill="none" stroke="#e2a53c" stroke-width="1.4"/><path d="M2 17C2 12 5 10.5 9 10.5S16 12 16 17" fill="none" stroke="#e2a53c" stroke-width="1.4"/></svg>
    <span>Marion Blake</span>
  </div>
  <div class="contact" style="top:1109px;left:446px">
    <svg viewBox="0 0 18 18" aria-hidden="true"><path d="M4 2L7 5L5.5 7.5C6.5 9.5 8.5 11.5 10.5 12.5L13 11L16 14L14 16C8 16 2 10 2 4Z" fill="none" stroke="#e2a53c" stroke-width="1.4" stroke-linejoin="round"/></svg>
    <span>01632 960457 / 07700 900583</span>
  </div>
  <div class="contact" style="top:1132px;left:416px">
    <svg viewBox="0 0 18 18" aria-hidden="true"><rect x="1.5" y="3.5" width="15" height="11" fill="none" stroke="#e2a53c" stroke-width="1.4"/><path d="M1.5 3.5L9 10L16.5 3.5" fill="none" stroke="#e2a53c" stroke-width="1.4"/></svg>
    <span>marion@silverferngatherings.co.uk</span>
  </div>

  <nav class="base-nav">
    <span>Weddings</span><span>/</span>
    <span>Birthdays</span><span>/</span>
    <span>Conferences</span><span>/</span>
    <span>Product Launches</span><span>/</span>
    <span>Fashion Shows</span><span>/</span>
    <span>Conventions</span>
  </nav>
</main>
</body>
</html>
```